RWM Electrical Business Card Design

Have a logo to use, just looking for design around this, would like green theme, would like symbols in place of phone, fax, email etc.

Business

RWM Electrical, Marcus Thorley, marcus@rwmelectrical.example.au, www.rwmelectrical.example.au, mobile 0491 568 342, phone (07) 3915 4280, fax (07) 3915 4280, facebook and linkedin
addresses

```html
<!DOCTYPE html>
<html lang="en">
<head>
<meta charset="utf-8">
<title>RWM Electrical – Business Card</title>
<link rel="stylesheet" href="https://fonts.googleapis.com/css2?family=Arimo&family=Open+Sans&display=swap">
<style>
  :root {
    --card-black: #050607;
    --signal-green: #3ee21c;
    --strand-blue: #3b4f78;
    --strand-glow: #8494b8;
    --mark-violet: #6c5fae;
    --mark-navy: #1d1f4a;
  }
  * { margin: 0; padding: 0; box-sizing: border-box; }
  html, body { width: 1200px; height: 741px; overflow: hidden; background: var(--card-black); }
  .card {
    position: relative;
    width: 1200px;
    height: 741px;
    background: var(--card-black);
    overflow: hidden;
    font-family: "Open Sans", sans-serif;
    color: var(--signal-green);
  }
  .light-strands {
    position: absolute;
    left: 43px; top: 230px;
    width: 1115px; height: 320px;
    background:
      radial-gradient(ellipse 50% 18% at 62% 45%, rgba(132,148,184,0.30), transparent 70%),
      radial-gradient(ellipse 70% 38% at 50% 48%, rgba(59,79,120,0.50), transparent 75%);
    filter: blur(6px);
  }
  .line { position: absolute; line-height: 1; white-space: nowrap; }
  .brand-dot {
    position: absolute;
    left: 105px; top: 90px;
    width: 124px; height: 124px;
    border-radius: 50%;
    background: var(--mark-violet);
    border: 10px solid var(--mark-navy);
  }
  .brand-name { left: 243px; top: 119px; font-family: "Arimo", sans-serif; font-size: 60px; }
  .owner-name { right: 543px; top: 176px; font-size: 38px; }
  .services { left: 117px; top: 214px; font-size: 26px; }
  .centre {
    left: 100px; width: 1000px;
    display: flex; justify-content: center; align-items: center; gap: 12px;
  }
  .icon { width: 26px; height: 26px; fill: none; stroke: var(--signal-green); stroke-width: 2; flex: none; }
  .icon-solid { fill: var(--signal-green); stroke: none; }
  .sep { width: 26px; }
  .contact-heading { top: 335px; font-size: 41px; }
  .email { top: 384px; font-size: 30px; }
  .phone { top: 422px; font-size: 30px; }
  .mobile-fax { top: 460px; font-size: 28px; }
  .website { top: 524px; font-size: 41px; }
  .tagline { top: 571px; font-size: 38px; }
  .location { top: 622px; font-size: 31px; }
  .social { top: 672px; font-size: 24px; }
  .social-box { width: 22px; height: 22px; background: var(--signal-green); border-radius: 4px; flex: none; }
</style>
</head>
<body>
  <div class="card">
    <div class="light-strands" role="img" aria-label="Flowing blue light strands across the card"></div>

    <div class="brand-dot"></div>
    <div class="line brand-name">RWM Electrical</div>
    <div class="line owner-name">Marcus Thorley</div>
    <div class="line services">Construction Works Contracts &amp; Service Work</div>

    <div class="line centre contact-heading">Contact Us By Phone or Email:</div>
    <div class="line centre email">
      <svg class="icon" viewBox="0 0 24 24" aria-hidden="true"><rect x="2" y="5" width="20" height="14" rx="1.5"/><path d="M2.5 6l9.5 7 9.5-7"/></svg>
      <span>marcus@rwmelectrical.example.au</span>
    </div>
    <div class="line centre phone">
      <svg class="icon" viewBox="0 0 24 24" aria-hidden="true"><path d="M6.5 2.5l3 4-2 2.5a13 13 0 0 0 7.5 7.5l2.5-2 4 3-2 4C12 21.5 2.5 12 4 4.5z"/></svg>
      <span>(07) 3915 4280</span>
    </div>
    <div class="line centre mobile-fax">
      <svg class="icon" viewBox="0 0 24 24" aria-hidden="true"><rect x="6" y="2" width="12" height="20" rx="2"/><path d="M10 18.5h4"/></svg>
      <span>0491 568 342</span>
      <span class="sep"></span>
      <svg class="icon" viewBox="0 0 24 24" aria-hidden="true"><rect x="3" y="9" width="18" height="10" rx="1.5"/><path d="M7 9V3h10v6M7 15h10"/></svg>
      <span>(07) 3915 4280</span>
    </div>

    <div class="line centre website">www.rwmelectrical.example.au</div>
    <div class="line centre tagline">Qualified &amp; Experienced Electrician</div>
    <div class="line centre location">Located In: Marrowbank Station, via Tallowvale</div>
    <div class="line centre social">
      <span class="social-box"></span><span>/rwmelectrical</span>
      <span class="sep"></span>
      <span class="social-box"></span><span>/marcus-thorley</span>
    </div>
  </div>
</body>
</html>
```